"Lantern Field" Play - Poster Design for Theatre Group

We are an amateur theatre group based in Geneva, Switzerland. We take pride in eye-catching posters for our shows, which are printed in various sizes.
This design will be for a play in March 2016. The play is called "Lantern Field", and it's a Harwick Medal winner from Marcus Ellery-Pound. The play is about a couple who have everything a family could want, until they lose a child in a life-shattering accident that turns their world upside down. The play charts the couple's bittersweet search to find each other and to find comfort.
Most importantly, we want a design that will make people want to see the show. We don't want to give away the plot or be too heavy-handed about death, but we want it to be clear that it's not a comedy (although there are some lighter moments!).
Attached you will find a template for the poster. This simply has our group name and logo in the top right corner: (Lakeshore Stage Players Circle presents).
You may change the color of both the text and the logo, but please do not change the font, size, or location.
Here is the information that needs to be on the poster, wherever you see fit:
play title: Lantern Field
author byline: by Marcus Ellery-Pound
director line: directed by Rob Feltwick
tagline: How do you keep it together when your whole world's fallen apart?
dates and times:
1-5 March 2016
(Tue-Fri 20:00, Sat 19:00)
location:
Théâtre du Vieux-Moulin
Eaux-Vives, Geneva
websites:
www.lspc.ch
www.scenelettres.ch
Technical Details:
Any font or combination of fonts is acceptable. The largest text should be the play title. The author's name must be at least 50% of the title font size.
For this competition, we would like the version with A3 proportions, which will also be used at F4 (89.5 x 128 cm) and A5 sizes (14.8 x 21 cm). Therefore no text should be below 9pt at A5.
However, from the winning designer we will also need repurposed sizes of the same design. Here is a comprehensive list of the sizes we will need.
1) A3 print poster. Artwork should be 300dpi, CMYK, sent with a 1mm bleed all round, to specification PDF/X-1A:2001. We will need this image in PDF format in addition to the default Artbrigade formats.
2) Chatterly advert picture. 1200px by 628px, RGB jpeg. This must comply with Chatterly’s restrictions on amount of text, which is no more than 20% of area taken up by text.(https://www.chatterly.example/ads/tools/text_overlay).
Because of these restrictions it is sufficient to include just the title and the author's name in this version.
3) Chatterly cover picture: 851px by 314px. RGB jpeg. It is sufficient to include just the title and the author's name in this version.
4) Web banner. 1000px by 300px. RGB jpeg. This version should include just the main image(s), no text.
Theatergoers
Entertainment

```html
<!DOCTYPE html>
<html lang="en">
<head>
<meta charset="utf-8">
<title>Lantern Field — Poster</title>
<link rel="stylesheet" href="https://fonts.googleapis.com/css2?family=Roboto+Condensed:ital,wght@0,400;0,700;1,400&display=swap">
<style>
  :root {
    --sky: #8fb5b8;
    --ink: #1d2740;
    --paper: #ffffff;
    --art-light: #b7cfcf;
    --art-warm: #d9b7a8;
    --art-deep: #5f6f86;
  }
  * { margin: 0; padding: 0; box-sizing: border-box; }
  html, body { width: 865px; height: 1200px; overflow: hidden; }
  body { background: var(--sky); }
  .poster {
    position: relative;
    width: 865px;
    height: 1200px;
    background: var(--sky);
    font-family: "Roboto Condensed", "Arial Narrow", sans-serif;
    overflow: hidden;
  }
  .couple-art {
    position: absolute;
    left: 55px;
    top: 280px;
    width: 790px;
    height: 700px;
    background:
      radial-gradient(ellipse at 28% 60%, var(--art-warm) 0%, transparent 45%),
      radial-gradient(ellipse at 72% 45%, var(--art-deep) 0%, transparent 50%),
      radial-gradient(ellipse at 50% 50%, var(--art-light) 0%, transparent 70%);
    opacity: 0.85;
  }
  .director {
    position: absolute;
    left: 58px;
    top: 46px;
    font-style: italic;
    font-size: 34px;
    color: var(--paper);
  }
  .presenter {
    position: absolute;
    top: 30px;
    right: 24px;
    display: flex;
    align-items: center;
    gap: 14px;
  }
  .presenter-name {
    text-align: right;
    font-weight: 700;
    font-size: 20px;
    line-height: 1.15;
    color: var(--ink);
  }
  .presenter-mark {
    width: 64px;
    height: 64px;
    border-radius: 50%;
    background: var(--paper);
  }
  .title {
    position: absolute;
    left: 48px;
    top: 130px;
    font-weight: 400;
    font-size: 150px;
    line-height: 0.9;
    letter-spacing: -1px;
    color: var(--paper);
    text-transform: uppercase;
  }
  .byline {
    position: absolute;
    left: 40px;
    right: 40px;
    top: 950px;
    text-align: center;
    font-weight: 700;
    font-size: 76px;
    line-height: 1;
    white-space: nowrap;
    color: var(--ink);
  }
  .details {
    position: absolute;
    left: 40px;
    top: 1048px;
    width: 380px;
    font-size: 21px;
    line-height: 1.2;
    color: var(--ink);
  }
  .details .dates { font-weight: 700; }
  .tagline {
    position: absolute;
    right: 38px;
    top: 1052px;
    width: 390px;
    text-align: right;
    font-size: 26px;
    line-height: 1.18;
    color: var(--ink);
  }
</style>
</head>
<body>
  <main class="poster">
    <div class="couple-art" role="img" aria-label="Illustration of a couple holding hands, with the empty outline of a child standing between them"></div>

    <p class="director">directed by Rob Feltwick</p>

    <div class="presenter">
      <p class="presenter-name">Lakeshore Stage<br>Players Circle<br>presents</p>
      <span class="presenter-mark"></span>
    </div>

    <h1 class="title">Lantern<br>Field</h1>

    <p class="byline">by Marcus Ellery-Pound</p>

    <div class="details">
      <p class="dates">1–5 March 2016</p>
      <p class="times">Tue–Fri 20:00, Sat 19:00</p>
      <p class="venue">Théâtre du Vieux-Moulin, Eaux-Vives, Geneva</p>
      <p class="web">www.lspc.ch · www.scenelettres.ch</p>
    </div>

    <p class="tagline">How do you keep it together when your whole world's fallen apart?</p>
  </main>
</body>
</html>
```